KT Holloway Insurance Group, LLC - Branding Project

We have an existing business card that was designed on Pelma Press. We recently completed a new logo design with sketch harbor and would like to utilize this new logo design into a business card design. Our new logo will be a major emphasis of our branding that is currently under development.

We are an independent insurance agency licensed in Colorado. We specialized in four keys areas. Business Insurance, Risk Management, Employee Benefits and Investments.

We would like the efforts of this design to last for 5 years minimum. Existing business card and new logo design files attached.

Industry/Entity Type

Business

Contact Information for Business Card

See attached files for existing business card design.

Requirements
Must have
• My office is a virtual office. All of our marketing effort drive from the Denver, CO office location. Our mailing address is just for mailing, that's it.
• Please maintain the color scheme of the new logo design.
Nice to have
• Doublesided card, I think? Your the expert if you have other ideas that are better I am excited to see them.

```html
<!DOCTYPE html>
<html lang="en">
<head>
<meta charset="utf-8">
<title>KT Holloway Insurance Group – Stationery</title>
<link href="https://fonts.googleapis.com/css2?family=Questrial&family=Open+Sans:wght@400;700&display=swap" rel="stylesheet">
<style>
  :root {
    --bg: #dcdcdc;
    --paper: #f7f7f7;
    --navy: #2b2568;
    --navy-light: #353085;
    --blue: #0f9ad8;
    --ink: #3a3a3a;
    --muted: #6a6a6a;
    --rule: #9a9a9a;
  }
  * { margin: 0; padding: 0; box-sizing: border-box; }
  html, body { width: 1200px; height: 1000px; overflow: hidden; }
  body { background: var(--bg); position: relative; font-family: "Open Sans", Arial, sans-serif; color: var(--ink); }

  .sheet { position: absolute; background: var(--paper); overflow: hidden; }

  .brand { position: absolute; display: flex; align-items: center; gap: 8px; }
  .brand-dot { border-radius: 50%; background: var(--blue); flex: none; }
  .brand-name { font-family: "Questrial", sans-serif; color: var(--navy); line-height: 1.1; }
  .brand-name span { display: block; }

  .corner-disc { position: absolute; border-radius: 50%; background: var(--blue); }

  /* Folder */
  .folder { left: 152px; top: 40px; width: 458px; height: 560px; border-radius: 4px;
    background: linear-gradient(180deg, var(--navy) 0%, var(--navy-light) 100%); }
  .folder .spine { position: absolute; left: 22px; top: 0; bottom: 0; width: 1px; background: rgba(255,255,255,.15); }
  .folder .brand { left: 110px; top: 70px; }
  .folder .brand-name { color: #ffffff; font-size: 22px; }
  .folder .brand-name span + span { font-size: 12px; letter-spacing: 1px; }
  .folder .corner-disc { width: 200px; height: 200px; left: 129px; bottom: -100px; }

  /* Letterhead */
  .letterhead { left: 616px; top: 60px; width: 417px; height: 540px; }
  .letterhead .brand { left: 38px; top: 42px; }
  .letterhead .brand-name { font-size: 14px; }
  .letterhead .brand-name span + span { font-size: 8px; letter-spacing: .8px; }
  .letter-body { position: absolute; left: 38px; top: 181px; width: 354px; font-size: 5.6px; line-height: 1.42; text-align: justify; color: var(--ink); }
  .letter-body p { margin-bottom: 6px; }
  .sign-off { margin-top: 8px; }
  .sign-off strong { display: block; }
  .signature { position: absolute; left: 88px; top: 350px; width: 90px; height: 40px; }
  .letter-footer { position: absolute; left: 38px; right: 60px; top: 503px; border-top: 1px solid var(--rule); padding-top: 5px;
    font-size: 5.5px; line-height: 1.5; display: flex; justify-content: space-between; }
  .letter-footer .web { align-self: flex-start; }
  .letter-footer b, .accent { color: var(--blue); font-weight: 400; }
  .letterhead .corner-disc { width: 50px; height: 50px; right: -20px; top: 465px; }

  /* Envelopes */
  .envelope-front { left: 117px; top: 629px; width: 466px; height: 202px; }
  .envelope-front .brand { left: 22px; top: 25px; }
  .envelope-front .brand-name { font-size: 15px; }
  .envelope-front .brand-name span + span { font-size: 8px; letter-spacing: .8px; }
  .return-address { position: absolute; left: 22px; top: 78px; font-size: 6.5px; line-height: 1.4; }
  .envelope-front .corner-disc { width: 90px; height: 90px; right: -40px; top: 55px; }

  .envelope-back { left: 616px; top: 629px; width: 467px; height: 202px; }
  .envelope-back .flap { position: absolute; inset: 0; width: 467px; height: 202px; }
  .envelope-back .seal { position: absolute; left: 224px; top: 19px; width: 22px; height: 22px; border-radius: 50%; background: var(--blue); }

  /* Business cards */
  .card-front { left: 410px; top: 860px; width: 198px; height: 100px; }
  .card-front .brand { left: 10px; top: 15px; gap: 4px; }
  .card-brand .brand-dot { width: 10px; height: 10px; }
  .card-brand .brand-name { font-size: 7.5px; }
  .card-brand .brand-name span + span { font-size: 4px; letter-spacing: .4px; }
  .card-person { position: absolute; left: 10px; top: 50px; font-size: 4px; line-height: 1.45; }
  .card-person .name { color: var(--blue); font-size: 5.5px; font-weight: 700; }
  .card-person .title { font-size: 3.8px; margin-bottom: 4px; }
  .card-front .corner-disc { width: 46px; height: 46px; right: -12px; top: 27px; }

  .card-back { left: 616px; top: 860px; width: 173px; height: 100px; }
  .card-back .brand { left: 80px; top: 15px; gap: 4px; }
  .card-back .corner-disc { width: 46px; height: 46px; left: -24px; top: 27px; }
  .card-address { position: absolute; right: 12px; top: 69px; font-size: 4px; line-height: 1.45; text-align: right; }
</style>
</head>
<body>

  <section class="sheet folder" aria-label="Presentation folder">
    <div class="spine"></div>
    <div class="brand">
      <div class="brand-dot" style="width:50px;height:50px"></div>
      <div class="brand-name"><span>KT Holloway</span><span>Insurance Group</span></div>
    </div>
    <div class="corner-disc"></div>
  </section>

  <section class="sheet letterhead" aria-label="Letterhead">
    <div class="brand">
      <div class="brand-dot" style="width:30px;height:30px"></div>
      <div class="brand-name"><span>KT Holloway</span><span>Insurance Group</span></div>
    </div>
    <div class="letter-body">
      <p><strong style="font-size:6.5px">Dear sir,</strong></p>
      <p>Communication is a very integral part of living creatures, animals and humans. Communication may be verbal or written. Written communication however is only applicable to human beings. Can you even imagine a world without communication? Verbal communication can be through telephones, webcams or in person. Written communication is through letters, emails and mobile phone messages.</p>
      <p>In today's world of great inventions and technology, letters have somehow become redundant. It is the time for text messages or chats. But they still can communicate a lot more than all other modes of communication. Organizations and various government departments still bank on letters as a strong medium of communication. There is no comparison in costs of sending letters as compared to costs of mobile phone messages though – letters are far cheaper. Letters now commonly known as "hard copy documents" are considered more relevant and important than email copies of text messages as proof or evidence of some sort.</p>
      <p>Letters speak volumes about a person or an organization that writes it. So one must take utmost care ensuring that the language used in any letter is appropriate for the occasion for which it is being written. Since a letter is also a written proof or document, if there are certain things that should not form a part of it, then that too should be carefully handled.</p>
      <p>Writing a good letter is an art. But if for some reason someone is unable to write that perfect letter, these different types of letters provide a base for you to build on. Sample letters have been given for everyone to understand what all information needs to form a part of the letter type and then it can be customized.</p>
      <div class="sign-off">Yours Sincerely,<strong>Dana Merrow</strong></div>
    </div>
    <svg class="signature" viewBox="0 0 90 40" aria-hidden="true">
      <path d="M4 28 C10 10 14 12 12 30 C18 14 22 14 20 30 C26 18 30 20 32 26 C36 16 40 18 40 26 L52 12 C50 22 48 32 52 36 M46 18 L72 14 M58 16 C62 26 64 22 70 24" fill="none" stroke="#3a46a0" stroke-width="1"/>
    </svg>
    <div class="letter-footer">
      <div>22 Larkin Plaza, 1800 Elm Street, Suite 300, Denver, CO 80205<br>
        <b>T:</b> 970.555.0142 · <b>F:</b> 970.555.0147 · <b>E:</b> kevin@ktholloway-ins.com</div>
      <div class="web">www.<span class="accent">ktholloway-ins</span>.com</div>
    </div>
    <div class="corner-disc"></div>
  </section>

  <section class="sheet envelope-front" aria-label="Envelope front">
    <div class="brand">
      <div class="brand-dot" style="width:36px;height:36px"></div>
      <div class="brand-name"><span>KT Holloway</span><span>Insurance Group</span></div>
    </div>
    <div class="return-address">PO Box 417<br>Millbrook, CO 80599</div>
    <div class="corner-disc"></div>
  </section>

  <section class="sheet envelope-back" aria-label="Envelope back">
    <svg class="flap" viewBox="0 0 467 202" aria-hidden="true">
      <path d="M0 62 L20 68 L447 68 L467 40" fill="none" stroke="#e2e2e2" stroke-width="1"/>
    </svg>
    <div class="seal"></div>
  </section>

  <section class="sheet card-front" aria-label="Business card front">
    <div class="brand card-brand">
      <div class="brand-dot"></div>
      <div class="brand-name"><span>KT Holloway</span><span>Insurance Group</span></div>
    </div>
    <div class="card-person">
      <div class="name">KEVIN HOLLOWAY</div>
      <div class="title">ACCOUNT EXECUTIVE</div>
      <div><span class="accent">T:</span> 970.555.0142 · <span class="accent">F:</span> 970.555.0147</div>
      <div><span class="accent">E:</span> kevin@ktholloway-ins.com</div>
      <div><span class="accent">W:</span> www.ktholloway-ins.com</div>
    </div>
    <div class="corner-disc"></div>
  </section>

  <section class="sheet card-back" aria-label="Business card back">
    <div class="brand card-brand">
      <div class="brand-dot"></div>
      <div class="brand-name"><span>KT Holloway</span><span>Insurance Group</span></div>
    </div>
    <div class="card-address">22 Larkin Plaza, 1800 Elm Street<br>Suite 300, Denver, CO 80205</div>
    <div class="corner-disc"></div>
  </section>

</body>
</html>
```